Larkmoor Pawn Shop Moving

My pawn shop will be relocating on August 1st 2012. We are moving 1 block north at the corner of Dorrance and Wexcombe Ave. Next to Crumblo. The new location will include bigger facilities and shopping area. The new address is 4820 N Dorrance Rd, Harlow Grove, IL 60387 708-519-GOLD (4653). I would like to see a neon light border, with dollar symbols at each corner. I would also like to print 2 per page, so thinking 8.5 x 5.5 with the design running horizontal.

```html
<!DOCTYPE html>
<html lang="en">
<head>
<meta charset="utf-8">
<title>Larkmoor Pawn Shop – We Are Moving</title>
<link rel="stylesheet" href="https://fonts.googleapis.com/css2?family=Bowlby+One+SC&family=Orbitron:wght@900&family=Nunito:wght@900&family=Montserrat:wght@700&display=swap">
<style>
  :root {
    --night: #000000;
    --neon: #27f05a;
    --note-light: #c9d6c4;
    --note-mid: #8fa48a;
    --panel-top: #26352a;
    --panel-bottom: #17211a;
    --gold-light: #fff3a0;
    --gold: #f2c62a;
    --gold-deep: #a8740a;
    --ink: #1a1405;
    --address-green: #3dff5c;
  }
  html, body { margin: 0; padding: 0; overflow: hidden; background: var(--night); }
  .flyer {
    position: relative;
    width: 1200px; height: 846px; overflow: hidden;
    background: radial-gradient(ellipse at center, #0a3a12 0%, #05200a 55%, #000 100%);
  }
  .neon-frame {
    position: absolute; left: 42px; top: 30px; width: 1110px; height: 782px;
    box-sizing: border-box;
    border: 14px solid var(--neon);
    box-shadow: 0 0 18px 6px var(--neon), inset 0 0 18px 6px var(--neon);
    background: #06240c;
  }
  .note-border {
    position: absolute; left: 82px; top: 62px; width: 1030px; height: 720px;
    background: linear-gradient(135deg, var(--note-light), var(--note-mid) 50%, var(--note-light));
  }
  .panel {
    position: absolute; left: 150px; top: 128px; width: 898px; height: 590px;
    background: linear-gradient(var(--panel-top), var(--panel-bottom));
    box-shadow: inset 0 0 0 2px #55684f;
  }
  .corner {
    position: absolute; width: 124px; height: 186px; border-radius: 50%;
    background: radial-gradient(ellipse at 40% 35%, #3a3a3a, #050505 70%);
    box-shadow: 0 0 0 3px #0d0d0d, 0 4px 10px rgba(0,0,0,.6);
    display: flex; align-items: center; justify-content: center;
    font-family: "Bowlby One SC", sans-serif; font-size: 130px; line-height: 1;
    color: var(--gold);
    text-shadow: 3px 3px 0 var(--gold-deep), 5px 6px 4px rgba(0,0,0,.7);
  }
  .corner--tl { left: 96px;  top: 74px; }
  .corner--tr { left: 978px; top: 74px; }
  .corner--bl { left: 96px;  top: 580px; }
  .corner--br { left: 978px; top: 580px; }
  .gold {
    background: linear-gradient(var(--gold-light), var(--gold) 45%, var(--gold-deep) 100%);
    -webkit-background-clip: text; background-clip: text; color: transparent;
  }
  .moving-pill {
    position: absolute; left: 258px; top: 140px; width: 670px; height: 78px;
    border-radius: 40px;
    background: linear-gradient(#5a5f5a, #1e221e 55%, #3a3f3a);
    box-shadow: 0 0 0 3px #1a1a1a, 0 6px 10px rgba(0,0,0,.6);
    display: flex; align-items: center; justify-content: center;
  }
  .moving-pill__text {
    font-family: "Orbitron", sans-serif; font-weight: 900; font-size: 44px; letter-spacing: 1px;
    -webkit-text-stroke: 1px var(--ink);
  }
  .headline {
    position: absolute; left: 150px; width: 898px; margin: 0; text-align: center;
    font-family: "Bowlby One SC", sans-serif; font-weight: 400;
    -webkit-text-stroke: 2px var(--ink);
    filter: drop-shadow(0 0 10px rgba(80,255,90,.55));
  }
  .headline--name { top: 232px; font-size: 104px; line-height: 1; }
  .headline--trade { top: 345px; font-size: 62px; line-height: 1; }
  .directions {
    position: absolute; left: 150px; top: 428px; width: 898px; margin: 0; text-align: center;
    font-family: "Nunito", sans-serif; font-weight: 900; font-size: 50px; line-height: 52px;
    letter-spacing: 0.5px;
    -webkit-text-stroke: 1.5px var(--ink);
  }
  .landmark {
    position: absolute; left: 150px; top: 540px; width: 898px; text-align: center;
    font-family: "Montserrat", sans-serif; font-weight: 700; font-size: 18px; color: var(--gold);
  }
  .address {
    position: absolute; left: 150px; top: 596px; width: 898px; text-align: center;
    font-family: "Montserrat", sans-serif; font-weight: 700; font-size: 28px; color: var(--address-green);
  }
  .phone {
    position: absolute; left: 150px; top: 642px; width: 898px; text-align: center;
    font-family: "Orbitron", sans-serif; font-weight: 900; font-size: 34px;
    -webkit-text-stroke: 1px var(--ink);
    filter: drop-shadow(0 0 6px rgba(80,255,90,.8));
  }
</style>
</head>
<body>
<main class="flyer">
  <div class="neon-frame"></div>
  <div class="note-border" role="img" aria-label="Banknote-style engraved border pattern"></div>
  <div class="panel"></div>

  <div class="corner corner--tl">$</div>
  <div class="corner corner--tr">$</div>
  <div class="corner corner--bl">$</div>
  <div class="corner corner--br">$</div>

  <div class="moving-pill"><span class="moving-pill__text gold">WE ARE MOVING</span></div>

  <h1 class="headline headline--name gold">LARKMOOR</h1>
  <h2 class="headline headline--trade gold">PAWN SHOP</h2>

  <p class="directions gold">1 block north at the corner of<br>Dorrance and Wexcombe Ave</p>
  <div class="landmark">NEXT TO CRUMBLO</div>

  <div class="address">4820 N DORRANCE RD, HARLOW GROVE, IL 60387</div>
  <div class="phone gold">708-519-GOLD (4653)</div>
</main>
</body>
</html>
```